Buch-/E-Book-Cover für Kinderbuch zum spielerischen Umgang zwischen Kind und Hund
Zielgruppe
Die Zielgruppe sind Kinder die lernen möchten mit Ihrem Hund besser zu spielen, verstehen und erziehen. Es ist ein Kinderbuch und das Buch soll dementsprechend 'kinderlicher' gestaltet sein.
Ich habe kein eigenes Konzept für das Cover mir derzeitig überlegt und ich werde die erstellten Cover bei meiner Zielgruppe testen und danach den Gewinner küren.
In diesem Buch handelt sich um ein Sachbuch zum Thema Hundeerziehung für Kinder. Ich möchte Ihnen die Inhaltsangabe, Vorwort und Buchrückseite mitteilen. Das Buch werde ich auf Bucharo.de veröffentlichen. Außerdem möchte ich Ihnen die 2 größten Konkurrenten vorstellen.
Das Vorwort:
Vorwort
Der Hund ist für das Kind mehr als nur ein vierbeiniger Hausgenosse mit Kuschelfaktor, er ist ein echter Partner zum Spielen und Lernen. Mit den passenden Ideen gestaltet sich der Alltag mit dem Tier richtig spannend. Sowohl Kind als auch Hund entwickeln sich Schritt für Schritt weiter und wachsen immer mehr zusammen. Für Jungen und Mädchen gibt es vielfältige Möglichkeiten, sich mit ihrem Vierbeiner zu beschäftigen. Kreative Rollenspiele gehören ebenso dazu wie das Lernen von Kunststücken, das Training von Intelligenz und Geschicklichkeit und das Basteln schöner Spielsachen. Lassen Sie sich von diesem Buch inspirieren und von den Fähigkeiten Ihrer Kinder und Hunde überraschen!
Gliederung:
Einleitung und Grundlegendes
1. Warum spielen Hunde und Kinder?
Gemeinsamkeiten zwischen Kind und Welpe
Die Vorteile einer engen Hund-Kind-Beziehung
Kind und Hund – das absolute Dream-Team?
Welcher Hund passt zum Kind?
Voraussetzungen für sicheres Spielen
2. Kreative Spiele
Kreative Beschäftigung mit dem Hund – darf das sein?
Rollenspiele mit Hunden
Das richtige Alter für Rollenspiele
Beispiele für typische Rollenspiele im Kindesalter
Tierische Rollenspiele – vom Kind zum Hund
Eigene Kommandos erfi..
Aufgabenstellung
Der Titel vom Buch lautet: Komm, lauf los! Wie junge Leser ihren Vierbeiner begreifen, lenken und mit ihm toben lernen.
Das sind die 2 größten Konkurrenten https://www.bucharo.de/Pfotenfibel-Junior/item/7712045839
https://www.bucharo.de/Bello-und-Ich-Ratgeber/item/7712093316
Das sind Cover auf dem Englisch sprachigen Markt die ich sehr gut finde
1. https://www.bucharo.example/item/5508812247
2. https://www.bucharo.example/item/5508867013

```html
<!DOCTYPE html>
<html lang="de">
<head>
<meta charset="utf-8">
<title>Komm, lauf los! – Buchcover</title>
<link rel="stylesheet" href="https://fonts.googleapis.com/css2?family=Bebas+Neue&family=Caveat+Brush&family=Montserrat:wght@600;800&family=Permanent+Marker&display=block">
<style>
  :root {
    --stage: #343434;
    --cover-orange: #ef7a0b;
    --cover-orange-deep: #e86c08;
    --cover-glow: #f0b200;
    --title-white: #f4f3f0;
    --title-shadow: rgba(170, 70, 0, 0.35);
    --ink: #0c0c0c;
    --band: #050505;
    --author-orange: #f58a12;
  }
  * { box-sizing: border-box; margin: 0; padding: 0; }
  html, body {
    width: 1200px;
    height: 1200px;
    overflow: hidden;
    background: var(--stage);
  }
  .book-cover {
    position: absolute;
    left: 230px;
    top: 52px;
    width: 740px;
    height: 1096px;
    overflow: hidden;
    background:
      radial-gradient(ellipse 300px 340px at 52% 48%, var(--cover-glow) 0%, rgba(240,178,0,0) 100%),
      linear-gradient(180deg, var(--cover-orange-deep) 0%, var(--cover-orange) 40%, var(--cover-orange) 100%);
  }
  .title-main {
    position: absolute;
    left: 0;
    top: 86px;
    width: 100%;
    text-align: center;
    font-family: "Bebas Neue", "Oswald", sans-serif;
    font-weight: 400;
    font-size: 270px;
    line-height: 1;
    letter-spacing: 1px;
    color: var(--title-white);
    text-shadow: 4px 5px 0 var(--title-shadow);
  }
  .cover-illustration {
    position: absolute;
    left: 205px;
    top: 290px;
    width: 335px;
    height: 370px;
    border-radius: 46% 46% 40% 40%;
    background: linear-gradient(165deg, #e9e7e1 0%, #d7d4cc 35%, #6b70bd 62%, #4a2c22 100%);
    opacity: 0.85;
  }
  .title-script {
    position: absolute;
    left: 0;
    top: 600px;
    width: 100%;
    text-align: center;
    font-family: "Permanent Marker", "Caveat Brush", cursive;
    font-weight: 400;
    font-size: 112px;
    line-height: 1.1;
    color: var(--ink);
    transform: rotate(-4deg);
    white-space: nowrap;
  }
  .subtitle {
    position: absolute;
    left: 110px;
    top: 808px;
    width: 520px;
    font-family: "Montserrat", sans-serif;
    font-weight: 600;
    font-size: 27px;
    line-height: 1.22;
    text-align: center;
    color: var(--ink);
  }
  .author-band {
    position: absolute;
    left: 0;
    bottom: 0;
    width: 100%;
    height: 102px;
    background: var(--band);
    display: flex;
    align-items: center;
    justify-content: center;
  }
  .author-name {
    font-family: "Montserrat", sans-serif;
    font-weight: 800;
    font-size: 33px;
    letter-spacing: 1px;
    color: var(--author-orange);
  }
</style>
</head>
<body>
  <main class="book-cover">
    <h1 class="title-main">KOMM,</h1>
    <div class="cover-illustration" role="img" aria-label="Illustration: ein lachender weißer Hund und ein fröhlicher Junge im blauen T-Shirt, die nebeneinander springen"></div>
    <p class="title-script">LAUF LOS!</p>
    <p class="subtitle">Wie junge Leser ihren Vierbeiner begreifen, lenken und mit ihm toben lernen.</p>
    <footer class="author-band">
      <span class="author-name">AUTHOR</span>
    </footer>
  </main>
</body>
</html>
```